cleaning service

we are a cleaning company,

we have a current flyer but its very dull

I have attached it, can we make it look modern, maybe add pictures and colour

```html
<!DOCTYPE html>
<html lang="en">
<head>
<meta charset="utf-8">
<title>Cleaning Services by Maple Lane News – Tri-fold Brochure</title>
<link href="https://fonts.googleapis.com/css2?family=Montserrat:wght@500;700;800&family=Open+Sans:wght@400;600;700&family=Lobster+Two:ital,wght@1,700&display=swap" rel="stylesheet">
<style>
  :root {
    --burgundy: #7a1232;
    --burgundy-dark: #4e0a1f;
    --burgundy-light: #9a1f44;
    --gold: #c9a13b;
    --gold-light: #e6c56a;
    --gold-dark: #a47f22;
    --cream: #f4ecd6;
    --paper: #ffffff;
    --ink: #3b3b3b;
    --ink-soft: #6d6d6d;
    --backdrop: #e8e5e0;
  }
  * { box-sizing: border-box; margin: 0; padding: 0; }
  html, body { width: 1200px; height: 2400px; overflow: hidden; }
  body {
    background: var(--backdrop);
    font-family: "Open Sans", Arial, sans-serif;
    color: var(--ink);
    position: relative;
  }
  .spread {
    position: absolute;
    left: 50px;
    width: 1100px;
    height: 850px;
    display: grid;
    grid-template-columns: repeat(3, 1fr);
    box-shadow: 0 10px 30px rgba(0,0,0,.18);
  }
  .spread--outside { top: 170px; }
  .spread--inside { top: 1330px; }
  .panel { position: relative; overflow: hidden; background: var(--paper); }
  .panel + .panel { border-left: 1px solid rgba(0,0,0,.06); }

  .photo { position: absolute; left: 0; width: 100%; }
  .photo--house-family { top: 0; height: 520px; background: linear-gradient(180deg, #cfd6df 0%, #9aa7b6 35%, #c7b59a 62%, #6f8a4a 100%); }
  .photo--dining-room { top: 560px; height: 290px; background: linear-gradient(160deg, #f2f2ef 0%, #dcdcd6 50%, #b9b3a6 100%); }
  .photo--living-room { top: 0; height: 300px; background: linear-gradient(170deg, #f4f3ef 0%, #dedbd2 55%, #b8ad98 100%); }
  .photo--bedroom { top: 640px; height: 210px; background: linear-gradient(170deg, #f6f6f4 0%, #e1e3e2 55%, #b7c3c0 100%); }
  .circle-photo {
    position: absolute; border-radius: 50%;
    border: 4px solid var(--gold-light);
    box-shadow: 0 4px 10px rgba(0,0,0,.3);
  }
  .circle-photo--vacuum { width: 130px; height: 130px; right: 26px; top: 440px; background: radial-gradient(circle at 40% 40%, #d9d4cf, #8a7f78); }
  .circle-photo--carpet { width: 92px; height: 92px; left: 40px; top: 440px; background: radial-gradient(circle at 40% 40%, #f1e6a8, #b0954a); }
  .circle-photo--rug { width: 92px; height: 92px; left: 138px; top: 440px; background: radial-gradient(circle at 40% 40%, #e8e2d6, #9c8f7e); }
  .circle-photo--oven { width: 92px; height: 92px; left: 236px; top: 440px; background: radial-gradient(circle at 40% 40%, #f3d97a, #c38f2a); }

  .shape { position: absolute; left: 0; width: 100%; }

  .service { position: absolute; left: 30px; right: 30px; }
  .service__title {
    display: flex; align-items: center; gap: 10px;
    font-family: "Montserrat", Arial, sans-serif;
    font-weight: 700; font-size: 15px;
    color: var(--burgundy);
    margin-bottom: 8px;
  }
  .service__title--light { color: var(--gold-light); }
  .icon { width: 28px; height: 28px; flex: none; }
  .service__text { font-size: 10.5px; line-height: 1.5; color: var(--ink-soft); }
  .service__text--light { color: #f1dfe4; }

  .price-strip {
    margin-top: 10px;
    background: linear-gradient(90deg, var(--gold-dark), var(--gold-light), var(--gold-dark));
    color: #fff; font-size: 10.5px; font-weight: 700;
    padding: 5px 12px;
    display: flex; justify-content: space-between;
  }
  .price-strip--pale { background: var(--cream); color: var(--burgundy); font-weight: 600; border-top: 2px solid var(--gold); }

  .price-table { margin-top: 8px; background: var(--cream); padding: 8px 12px; width: 100%; border-collapse: collapse; font-size: 10.5px; }
  .price-table td { padding: 2px 0; color: var(--ink); }
  .price-table td:last-child { text-align: right; font-weight: 700; color: var(--burgundy); }
  .price-table--card { border: 2px solid var(--gold); }

  .about { position: absolute; left: 30px; right: 30px; top: 34px; }
  .about__title { font-family: "Montserrat", Arial, sans-serif; font-weight: 800; font-size: 22px; color: #fff; letter-spacing: 1px; margin-bottom: 14px; }
  .about__text { font-size: 11px; line-height: 1.6; color: #fff8e6; margin-bottom: 10px; }

  .brand { position: absolute; left: 0; right: 0; text-align: center; color: #fff; }
  .brand__main { font-family: "Montserrat", Arial, sans-serif; font-weight: 700; font-size: 27px; letter-spacing: 1px; }
  .brand__by { font-family: "Lobster Two", Georgia, cursive; font-style: italic; font-weight: 700; font-size: 30px; color: #fff; }

  .promo-text { position: absolute; left: 30px; right: 30px; top: 700px; text-align: center; font-size: 12.5px; line-height: 1.55; color: #fff; }

  .badge { position: absolute; right: 34px; top: 430px; width: 120px; height: 120px; }
  .badge__circle {
    position: absolute; inset: 0; border-radius: 50%;
    background: radial-gradient(circle at 40% 35%, var(--burgundy-light), var(--burgundy));
    border: 4px solid #fff; box-shadow: 0 4px 10px rgba(0,0,0,.3);
    text-align: center; color: #fff;
    font-family: "Montserrat", Arial, sans-serif; font-weight: 800;
    padding-top: 24px;
  }
  .badge__percent { font-size: 36px; line-height: 1; }
  .badge__percent small { font-size: 13px; }
  .badge__ribbon {
    position: absolute; left: -22px; right: -22px; top: 70px;
    background: linear-gradient(90deg, var(--gold-dark), var(--gold-light), var(--gold-dark));
    color: #fff; font-family: "Montserrat", Arial, sans-serif; font-weight: 800;
    font-size: 14px; text-align: center; padding: 4px 0; letter-spacing: 1px;
    transform: rotate(-12deg);
  }

  .call-pill {
    position: absolute; left: 28px; right: 28px;
    background: linear-gradient(90deg, var(--gold-dark), var(--gold-light), var(--gold-dark));
    border-radius: 18px; padding: 8px 14px;
    display: flex; align-items: center; justify-content: center; gap: 8px;
    font-family: "Montserrat", Arial, sans-serif; font-weight: 800; font-size: 13px; color: var(--burgundy-dark);
  }
  .call-pill svg { width: 14px; height: 14px; }
  .beat-price { position: absolute; left: 0; right: 0; text-align: center; font-family: "Montserrat", Arial, sans-serif; font-weight: 700; font-size: 13px; color: #fff; letter-spacing: 1px; }

  .call-line { position: absolute; left: 30px; right: 30px; top: 596px; display: flex; align-items: center; gap: 8px; font-family: "Montserrat", Arial, sans-serif; font-weight: 800; font-size: 13px; color: var(--ink); }
  .call-line svg { width: 14px; height: 14px; }

  .note { font-size: 10px; color: var(--ink-soft); margin-top: 6px; }
  .note--light { color: #f1dfe4; }
</style>
</head>
<body>

<!-- Outside of the tri-fold -->
<section class="spread spread--outside">

  <!-- Inner flap -->
  <article class="panel panel--flap">
    <div class="service" style="top:30px">
      <h3 class="service__title">
        <svg class="icon" viewBox="0 0 28 28"><rect width="28" height="28" rx="4" fill="var(--burgundy)"/><path d="M6 7h16M8 7v15M20 7v15M8 22c2-4 2-9 0-15M20 22c-2-4-2-9 0-15" stroke="#fff" stroke-width="1.8" fill="none"/></svg>
        Curtain Cleaning
      </h3>
      <p class="service__text">Our team takes down, cleans and rehangs curtains of every fabric, removing dust, odours and stains while keeping colours bright and hems neat.</p>
      <div class="price-strip"><span>Price per curtain</span></div>
      <table class="price-table">
        <tr><td>Small window</td><td>£8</td></tr>
        <tr><td>Large window</td><td>£12</td></tr>
      </table>
    </div>
    <div class="service" style="top:300px">
      <h3 class="service__title">
        <svg class="icon" viewBox="0 0 28 28"><rect width="28" height="28" rx="4" fill="var(--burgundy)"/><rect x="7" y="6" width="14" height="16" fill="none" stroke="#fff" stroke-width="1.8"/><path d="M14 6v16M7 14h14" stroke="#fff" stroke-width="1.8"/></svg>
        Window Cleaning
      </h3>
      <p class="service__text">We clean frames, sills and glass inside and out with streak-free products, leaving every pane sparkling and letting more light into your home.</p>
    </div>
    <div class="photo photo--dining-room" role="img" aria-label="Photo of a bright, clean dining room with a white table and chairs"></div>
    <svg class="shape" style="top:540px;height:60px" viewBox="0 0 367 60" preserveAspectRatio="none" aria-hidden="true">
      <path d="M0 0H367V14C250 52 110 52 0 22Z" fill="#fff"/>
      <path d="M0 22C110 52 250 52 367 14V22C250 60 110 60 0 30Z" fill="var(--gold)"/>
    </svg>
  </article>

  <!-- Back panel -->
  <article class="panel panel--back" style="background:linear-gradient(180deg,var(--gold-light),var(--gold) 45%,var(--gold-dark))">
    <div class="about">
      <h2 class="about__title">ABOUT US</h2>
      <p class="about__text">Maple Lane Cleaning Services offers professional home cleaning across the local area, with friendly staff who treat every house as their own.</p>
      <p class="about__text">We provide regular and one-off cleans to suit your routine and budget, using safe products and reliable equipment on every visit.</p>
      <p class="about__text">Every clean is checked before we leave, so you can relax knowing your home is fresh, tidy and ready for your family.</p>
    </div>
    <svg class="shape" style="top:460px;height:390px" viewBox="0 0 367 390" preserveAspectRatio="none" aria-hidden="true">
      <path d="M0 40C120 0 250 10 367 60V390H0Z" fill="var(--gold-light)"/>
      <path d="M0 50C120 10 250 20 367 70V390H0Z" fill="var(--burgundy)"/>
    </svg>
    <div class="circle-photo circle-photo--vacuum" role="img" aria-label="Round photo of a vacuum cleaner on a carpet"></div>
    <div class="brand" style="top:595px">
      <div class="brand__main">CLEANING SERVICES</div>
      <div class="brand__by">by Maple Lane News</div>
    </div>
    <p class="promo-text">We can integrate the cleaning services with the newspaper delivery services and at will are offering a 20% off for all our newspaper customers and £50 for introducing us to your family and friends.</p>
  </article>

  <!-- Front cover -->
  <article class="panel panel--cover" style="background:var(--burgundy)">
    <div class="photo photo--house-family" role="img" aria-label="Photo of a smiling family of four in front of their house"></div>
    <svg class="shape" style="top:430px;height:420px" viewBox="0 0 367 420" preserveAspectRatio="none" aria-hidden="true">
      <path d="M0 70C120 20 260 10 367 0V420H0Z" fill="var(--gold)"/>
      <path d="M0 82C120 32 260 22 367 14V420H0Z" fill="var(--burgundy)"/>
    </svg>
    <div class="badge">
      <div class="badge__circle"><div class="badge__percent">20<small>%</small></div></div>
      <div class="badge__ribbon">SPECIAL OFFER</div>
    </div>
    <div class="brand" style="top:600px">
      <div class="brand__main">CLEANING SERVICES</div>
      <div class="brand__by">by Maple Lane News</div>
    </div>
    <div class="call-pill" style="top:722px">
      PLEASE CALL US ON
      <svg viewBox="0 0 24 24"><path d="M6.6 10.8a15.1 15.1 0 0 0 6.6 6.6l2.2-2.2c.3-.3.7-.4 1-.2 1.1.4 2.3.6 3.6.6.6 0 1 .4 1 1V20c0 .6-.4 1-1 1A17 17 0 0 1 3 4c0-.6.4-1 1-1h3.5c.6 0 1 .4 1 1 0 1.2.2 2.4.6 3.6.1.3 0 .7-.2 1Z" fill="var(--burgundy-dark)"/></svg>
      07700 900123
    </div>
    <div class="beat-price" style="top:778px">TO BEAT ANY PRICE</div>
  </article>
</section>

<!-- Inside of the tri-fold -->
<section class="spread spread--inside">

  <!-- Left inside panel -->
  <article class="panel">
    <div class="photo photo--living-room" role="img" aria-label="Photo of a clean, modern living room with white sofas"></div>
    <svg class="shape" style="top:250px;height:70px" viewBox="0 0 367 70" preserveAspectRatio="none" aria-hidden="true">
      <path d="M0 10C120 50 250 50 367 20V70H0Z" fill="var(--gold)"/>
      <path d="M0 22C120 62 250 62 367 32V70H0Z" fill="#fff"/>
    </svg>
    <div class="service" style="top:340px">
      <h3 class="service__title">
        <svg class="icon" viewBox="0 0 28 28"><rect width="28" height="28" rx="4" fill="var(--burgundy)"/><circle cx="14" cy="14" r="5" fill="none" stroke="#fff" stroke-width="1.8"/><path d="M14 5v4M14 19v4M5 14h4M19 14h4M8 8l2.5 2.5M17.5 17.5 20 20M20 8l-2.5 2.5M10.5 17.5 8 20" stroke="#fff" stroke-width="1.6"/></svg>
        Antiviral Sanitisation Service
      </h3>
      <p class="service__text">Our sanitisation service uses approved disinfectants on handles, switches, worktops and other touch points, helping protect your household from germs and viruses.</p>
      <div class="price-strip price-strip--pale"><span>Including our cleaning materials</span><span>£16 (per hour)</span></div>
    </div>
    <div class="service" style="top:560px">
      <h3 class="service__title">
        <svg class="icon" viewBox="0 0 28 28"><rect width="28" height="28" rx="4" fill="var(--burgundy)"/><path d="M8 22h12M10 22V12h8v10M12 12V7h4v5" stroke="#fff" stroke-width="1.8" fill="none"/></svg>
        One Off Deep Cleaning Service
      </h3>
      <p class="service__text">A top-to-bottom clean of kitchens, bathrooms and living spaces, ideal before moving in or out, after building work, or as a seasonal refresh.</p>
      <div class="price-strip price-strip--pale"><span>Including our cleaning materials</span><span>£16 (per hour)</span></div>
    </div>
  </article>

  <!-- Middle inside panel -->
  <article class="panel" style="background:linear-gradient(180deg,var(--burgundy-light),var(--burgundy) 40%,var(--burgundy-dark))">
    <div class="service" style="top:30px">
      <h3 class="service__title service__title--light">
        <svg class="icon" viewBox="0 0 28 28"><rect width="28" height="28" rx="4" fill="var(--gold)"/><path d="M7 20h14M10 20V9h8v11" stroke="var(--burgundy)" stroke-width="1.8" fill="none"/></svg>
        Carpet Cleaning
      </h3>
      <p class="service__text service__text--light">We deep clean carpets with hot water extraction, lifting stains and allergens and leaving fibres soft, fresh and quick to dry.</p>
      <table class="price-table price-table--card">
        <tr><td>Single bedroom</td><td>£15</td></tr>
        <tr><td>Double bedroom</td><td>£20</td></tr>
        <tr><td>Living room</td><td>£25</td></tr>
        <tr><td>Dining room</td><td>£22</td></tr>
        <tr><td>Stairs</td><td>£20</td></tr>
        <tr><td>Landing</td><td>£10</td></tr>
        <tr><td>Hallway</td><td>£12</td></tr>
      </table>
      <p class="note note--light">Including our cleaning materials, minimum charge of £60</p>
    </div>
    <div class="circle-photo circle-photo--carpet" role="img" aria-label="Round photo of cleaning gloves and supplies"></div>
    <div class="circle-photo circle-photo--rug" role="img" aria-label="Round photo of a rug being vacuumed"></div>
    <div class="circle-photo circle-photo--oven" role="img" aria-label="Round photo of a cleaning spray and sponge"></div>
    <div class="service" style="top:560px">
      <h3 class="service__title service__title--light">
        <svg class="icon" viewBox="0 0 28 28"><rect width="28" height="28" rx="4" fill="var(--gold)"/><rect x="7" y="9" width="14" height="10" fill="none" stroke="var(--burgundy)" stroke-width="1.8"/></svg>
        Rug Cleaning
      </h3>
      <p class="service__text service__text--light">Rugs of every size and fibre are cleaned gently by hand to restore colour and texture.</p>
    </div>
    <div class="service" style="top:680px">
      <h3 class="service__title service__title--light">
        <svg class="icon" viewBox="0 0 28 28"><rect width="28" height="28" rx="4" fill="var(--gold)"/><rect x="7" y="7" width="14" height="14" fill="none" stroke="var(--burgundy)" stroke-width="1.8"/><rect x="10" y="12" width="8" height="6" fill="var(--burgundy)"/></svg>
        Oven Cleaning From £42
      </h3>
      <p class="service__text service__text--light">Ovens, hobs and extractor hoods are stripped, degreased and polished until they look like new.</p>
    </div>
  </article>

  <!-- Right inside panel -->
  <article class="panel">
    <div class="service" style="top:30px">
      <h3 class="service__title">
        <svg class="icon" viewBox="0 0 28 28"><rect width="28" height="28" rx="4" fill="var(--burgundy)"/><path d="M6 19v-6h16v6M8 13V9h12v4M6 19h16" stroke="#fff" stroke-width="1.8" fill="none"/></svg>
        Upholstery Cleaning
      </h3>
      <p class="service__text">Sofas, armchairs and dining chairs are cleaned to remove stains, odours and dust mites from fabric and cushions.</p>
      <div class="price-strip"><span>Price list</span></div>
      <table class="price-table">
        <tr><td>Armchair</td><td>£25</td></tr>
        <tr><td>Two-seater sofa</td><td>£40</td></tr>
        <tr><td>Three-seater sofa</td><td>£50</td></tr>
        <tr><td>Dining chair</td><td>£8</td></tr>
      </table>
      <p class="note">Including our cleaning materials, minimum charge of £40</p>
    </div>
    <div class="service" style="top:350px">
      <h3 class="service__title">
        <svg class="icon" viewBox="0 0 28 28"><rect width="28" height="28" rx="4" fill="var(--burgundy)"/><path d="M6 18h16v3M6 21v-9M9 15h5" stroke="#fff" stroke-width="1.8" fill="none"/></svg>
        Mattress Cleaning
      </h3>
      <p class="service__text">Mattresses are steam cleaned and sanitised on both sides to remove dust mites, sweat and stains.</p>
      <div class="price-strip"><span>Price list</span></div>
      <table class="price-table">
        <tr><td>Single mattress</td><td>£25</td></tr>
        <tr><td>Double mattress</td><td>£35</td></tr>
        <tr><td>King mattress</td><td>£40</td></tr>
      </table>
    </div>
    <div class="call-line">
      PLEASE CALL US ON
      <svg viewBox="0 0 24 24"><path d="M6.6 10.8a15.1 15.1 0 0 0 6.6 6.6l2.2-2.2c.3-.3.7-.4 1-.2 1.1.4 2.3.6 3.6.6.6 0 1 .4 1 1V20c0 .6-.4 1-1 1A17 17 0 0 1 3 4c0-.6.4-1 1-1h3.5c.6 0 1 .4 1 1 0 1.2.2 2.4.6 3.6.1.3 0 .7-.2 1Z" fill="var(--ink)"/></svg>
      07700 900123
    </div>
    <div class="photo photo--bedroom" role="img" aria-label="Photo of a tidy, light bedroom with a made bed"></div>
    <svg class="shape" style="top:625px;height:50px" viewBox="0 0 367 50" preserveAspectRatio="none" aria-hidden="true">
      <path d="M0 0H367V10C250 40 110 40 0 18Z" fill="#fff"/>
      <path d="M0 18C110 40 250 40 367 10V18C250 48 110 48 0 26Z" fill="var(--gold)"/>
    </svg>
  </article>
</section>

</body>
</html>
```